Sport Celebration Day Poster

The poster should highlight the sport of archery and bring awareness to the sport and invite people to come and try archery. We have a logo that must be featured, as well as a sample photos that can be used in the creative process, but do not necessarily have to be featured. The feel of the poster should be fun and inviting and have archery imagery (bows, arrows, targets, etc.).

The poster must feature the date MAY 11, 2019 and "Try Archery."

We would like to see an area where our sport clubs can fill in their own information including sections for "Name, Date, Location, Times, Location, Email, Website, and Notes."

Submissions should include some of these colours or colours from the logo:
Blue #00A1EF, Grey #313A43, Green #406C1D, Red #DC2F31, Yellow #FDDD39

```html
<!DOCTYPE html>
<html lang="en">
<head>
<meta charset="utf-8">
<title>Try Archery Poster</title>
<link rel="stylesheet" href="https://fonts.googleapis.com/css2?family=Alegreya+Sans:wght@500&family=Lato:wght@700&family=Oranienbaum&family=Oswald:wght@500&family=Vollkorn:wght@500&display=swap">
<style>
  :root {
    --stage: #cfcfcf;
    --board: #4e463b;
    --board-dark: #40392f;
    --red: #cc0a0a;
    --navy: #27255f;
    --yellow: #f6e03a;
    --white: #ffffff;
    --card: #d8cdbf;
    --ink: #1d1a17;
    --target-red: #c9262b;
    --wood: #b97a2c;
  }
  * { margin: 0; padding: 0; box-sizing: border-box; }
  html, body { width: 1200px; height: 1200px; overflow: hidden; background: var(--stage); }
  .poster {
    position: absolute; left: 184px; top: 62px; width: 834px; height: 1078px;
    background: radial-gradient(ellipse at 40% 30%, var(--board) 0%, var(--board-dark) 100%);
    box-shadow: 0 2px 6px rgba(0,0,0,.35);
    overflow: hidden;
  }
  .brand {
    position: absolute; left: 84px; top: 62px; width: 340px;
    font-family: "Lato", sans-serif; font-weight: 700; color: var(--white);
    line-height: 1; white-space: nowrap;
  }
  .brand-top { display: block; font-size: 24px; letter-spacing: 1px; padding-left: 4px; }
  .brand-main { display: block; font-size: 54px; letter-spacing: 2px; margin-top: 8px; }
  .target-art {
    position: absolute; left: 596px; top: 42px; width: 150px; height: 156px;
    background: radial-gradient(ellipse 45% 50% at 55% 45%, var(--white) 0 14%, var(--target-red) 15% 30%, var(--white) 31% 46%, var(--target-red) 47% 62%, var(--wood) 63% 75%, transparent 77%);
  }
  .title-band {
    position: absolute; left: 75px; top: 252px; width: 686px; height: 42px; background: var(--navy);
  }
  .title {
    position: absolute; left: 84px; top: 204px; width: 690px;
    font-family: "Vollkorn", serif; font-weight: 500; font-size: 108px; line-height: 1;
    color: var(--red); text-shadow: 3px 3px 0 #1a1620; white-space: nowrap;
  }
  .arrow { position: absolute; }
  .arrow-top { left: 122px; top: 318px; width: 590px; height: 64px; }
  .arrow-bottom { left: 274px; top: 1012px; width: 286px; height: 28px; }
  .prompt {
    position: absolute; left: 104px; top: 414px;
    font-family: "Alegreya Sans", sans-serif; font-weight: 500; font-size: 48px;
    color: var(--yellow); white-space: nowrap;
  }
  .archer-art {
    position: absolute; left: 0; top: 498px; width: 424px; height: 488px;
    background: radial-gradient(ellipse 50% 46% at 45% 52%, var(--red) 0 78%, rgba(204,10,10,.55) 90%, transparent 100%);
  }
  .info-card {
    position: absolute; left: 328px; top: 482px; width: 506px; height: 314px;
    background: var(--card);
    font-family: "Oranienbaum", serif; color: var(--ink);
  }
  .field { position: absolute; left: 20px; right: 40px; display: flex; align-items: baseline; font-size: 28px; line-height: 1; }
  .field .line { flex: 1; border-bottom: 2px dashed #3a332c; margin-left: 6px; height: 1px; }
  .field.name { top: 18px; font-size: 42px; }
  .field.date { top: 70px; }
  .field.time { top: 110px; }
  .field.location { top: 150px; }
  .field.extra { top: 190px; left: 44px; }
  .field.email { top: 230px; }
  .field.website { top: 278px; }
  .event-date {
    position: absolute; left: 440px; top: 894px;
    font-family: "Oswald", sans-serif; font-weight: 500; font-size: 64px; line-height: 1.1;
    color: var(--yellow); letter-spacing: 2px; white-space: nowrap;
  }
</style>
</head>
<body>
<main class="poster">
  <div class="brand"><span class="brand-top">ARCHERY LEAGUE</span><span class="brand-main">FLETCHWOOD</span></div>
  <div class="target-art" role="img" aria-label="Red and white archery target on a wooden stand with two arrows in the bullseye"></div>

  <div class="title-band"></div>
  <h1 class="title">Try, Archery!</h1>

  <svg class="arrow arrow-top" viewBox="0 0 590 64" aria-hidden="true">
    <line x1="40" y1="32" x2="540" y2="32" stroke="#fff" stroke-width="3"/>
    <polygon points="530,8 590,32 530,56" fill="#fff"/>
    <polygon points="0,20 60,32 0,44 20,32" fill="#fff"/>
    <polygon points="40,2 100,32 70,32" fill="#fff"/>
    <polygon points="40,62 100,32 70,32" fill="#fff"/>
    <polygon points="70,8 120,32 95,32" fill="#fff"/>
    <polygon points="70,56 120,32 95,32" fill="#fff"/>
  </svg>

  <p class="prompt">Fill in the following information:</p>

  <div class="archer-art" role="img" aria-label="Illustrated archer drawing a bow in navy and yellow over a red brush splash"></div>

  <section class="info-card">
    <div class="field name">Name :<span class="line"></span></div>
    <div class="field date">Date :<span class="line"></span></div>
    <div class="field time">Time :<span class="line"></span></div>
    <div class="field location">Location :<span class="line"></span></div>
    <div class="field extra"><span class="line"></span></div>
    <div class="field email">E-mail :<span class="line"></span></div>
    <div class="field website">Website :<span class="line"></span></div>
  </section>

  <p class="event-date">MAY 11, 2019</p>

  <svg class="arrow arrow-bottom" viewBox="0 0 286 28" aria-hidden="true">
    <line x1="20" y1="14" x2="250" y2="14" stroke="#fff" stroke-width="2"/>
    <polygon points="245,3 286,14 245,25" fill="#fff"/>
    <polygon points="0,5 40,14 0,23 10,14" fill="#fff"/>
    <polygon points="22,1 55,14 40,14" fill="#fff"/>
    <polygon points="22,27 55,14 40,14" fill="#fff"/>
  </svg>
</main>
</body>
</html>
```